New audiology website PSD design only - guaranteed

We need a clean and attractive website to replace an existing Audiology (hearing technology) website which will be wordpress based.
The current website is: http://pelmorahearing.com.au
They have a new logo and colors which you can find at www.quodel.net/temp/plh2018.pdf
We will no longer have a web shop in the new website
To enter the competition, we only need a sample of the home page.
The winning design will be asked to produce 2 standard page template alternatives as well (based on the winning home page design, but for a standard page layout)
The winning design must provide any photos used
We want a clean, credible site but with some warmth
Target Market(s)
All ages but needs to include the elderly
Industry/Entity Type
Medical And Science
Number of Pages Required
3 page
Look and feel
Each slider illustrates characteristics of the customer's brand and the style your logo design should communicate.

```html
<!DOCTYPE html>
<html lang="en">
<head>
<meta charset="utf-8">
<title>Pelmora Hearing – Home</title>
<link rel="stylesheet" href="https://fonts.googleapis.com/css2?family=Raleway:wght@300;400;600;700;800&family=Roboto:wght@300;400;500&display=swap">
<style>
  :root {
    --orange: #f37432;
    --ink: #333333;
    --text: #555555;
    --muted: #777777;
    --rule: #e8e8e8;
    --icon-ring: #c2aca4;
    --navy: #2a3240;
    --footer: #111418;
    --white: #ffffff;
  }
  * { box-sizing: border-box; margin: 0; padding: 0; }
  html, body { width: 1200px; height: 1200px; overflow: hidden; background: var(--white); }
  body { position: relative; font-family: "Roboto", sans-serif; color: var(--text); }

  .topbar { position: absolute; left: 0; top: 0; width: 1200px; height: 32px; border-bottom: 1px solid var(--rule); font-size: 10px; color: var(--muted); }
  .topbar .social { position: absolute; left: 132px; top: 11px; display: flex; gap: 20px; }
  .topbar .social span { width: 9px; height: 9px; border-radius: 50%; background: #9a9a9a; display: block; }
  .topbar .info { position: absolute; top: 8px; display: flex; align-items: center; gap: 6px; }
  .topbar .info svg { width: 12px; height: 12px; }
  .hours { left: 498px; }
  .phone { left: 676px; }
  .account { left: 864px; }

  .navbar { position: absolute; left: 0; top: 32px; width: 1200px; height: 50px; }
  .brand { position: absolute; left: 78px; top: 8px; display: flex; align-items: center; gap: 8px; font-family: "Raleway", sans-serif; font-weight: 600; font-size: 21px; color: var(--ink); }
  .brand .mark { width: 26px; height: 26px; border-radius: 50%; border: 2px solid var(--orange); }
  .menu { position: absolute; left: 320px; top: 18px; display: flex; font-size: 10.5px; color: var(--ink); }
  .menu a { color: inherit; text-decoration: none; position: relative; margin-right: 25px; }
  .menu a.active::after { content: ""; position: absolute; left: 0; right: -2px; top: 30px; height: 2px; background: var(--orange); }
  .search { position: absolute; left: 936px; top: 18px; display: flex; align-items: center; gap: 8px; font-size: 10.5px; color: #999; }

  .hero { position: absolute; left: 0; top: 82px; width: 1200px; height: 610px; overflow: hidden; }
  .hero-photo { position: absolute; inset: 0; background:
      linear-gradient(90deg, #ece9e7 0%, #f2f0ee 32%, #e9d6de 48%, #eddcd3 68%, #f0ece9 100%); }
  .hero-copy { position: absolute; left: 75px; top: 198px; font-family: "Raleway", sans-serif; }
  .hero-copy h1 { font-weight: 800; font-size: 44px; line-height: 46px; color: var(--ink); letter-spacing: -0.3px; }
  .hero-copy h1 .accent { color: var(--orange); }
  .hero-copy p { margin-top: 8px; font-size: 16px; color: var(--ink); font-family: "Roboto", sans-serif; }
  .btn { position: absolute; left: 5px; top: 142px; width: 95px; height: 34px; background: var(--orange); color: var(--white); font-family: "Roboto", sans-serif; font-weight: 500; font-size: 10.5px; display: flex; align-items: center; justify-content: center; }
  .appointment { position: absolute; left: 77px; top: 584px; width: 189px; height: 26px; background: var(--navy); color: var(--white); font-family: "Raleway", sans-serif; font-weight: 600; font-size: 11px; display: flex; align-items: center; justify-content: space-between; padding: 0 12px; }

  .welcome { position: absolute; left: 0; top: 720px; width: 1200px; text-align: center; font-family: "Raleway", sans-serif; }
  .welcome h2 { font-weight: 700; font-size: 19px; color: var(--ink); line-height: 22px; }
  .welcome h3 { font-weight: 400; font-size: 29px; color: #444; line-height: 32px; }
  .welcome .bar { width: 35px; height: 3px; background: var(--orange); margin: 8px auto 0; }
  .welcome p { width: 720px; margin: 18px auto 0; font-family: "Roboto", sans-serif; font-weight: 300; font-size: 10px; line-height: 18px; color: var(--text); }

  .service { position: absolute; top: 913px; width: 230px; text-align: center; }
  .service svg { width: 90px; height: 90px; display: block; margin: 0 auto; }
  .service h4 { margin-top: 24px; font-family: "Raleway", sans-serif; font-weight: 600; font-size: 14.5px; color: var(--ink); }
  .service p { margin-top: 10px; font-weight: 300; font-size: 10px; line-height: 18px; color: var(--text); padding: 0 12px; }
  .s1 { left: 87px; } .s2 { left: 415px; } .s3 { left: 743px; }

  .footer { position: absolute; left: 0; top: 1174px; width: 1200px; height: 26px; background: var(--footer); }
</style>
</head>
<body>
  <header class="topbar">
    <div class="social" aria-label="Social links"><span></span><span></span><span></span></div>
    <div class="info hours">
      <svg viewBox="0 0 12 12" fill="none" stroke="#f37432" stroke-width="1.2"><circle cx="6" cy="6" r="5"/><path d="M6 3v3l2 1"/></svg>
      Monday to Friday 9am to 5pm
    </div>
    <div class="info phone">
      <svg viewBox="0 0 12 12" fill="none" stroke="#f37432" stroke-width="1.2"><path d="M2 1.5l2 0 1 2.5-1.2 1a6 6 0 0 0 3.2 3.2l1-1.2 2.5 1v2a1 1 0 0 1-1 1A9 9 0 0 1 1 2.5a1 1 0 0 1 1-1z"/></svg>
      (02) 9000 0147 , 9000 0283
    </div>
    <div class="info account">
      <svg viewBox="0 0 12 12" fill="none" stroke="#f37432" stroke-width="1.2"><circle cx="6" cy="4" r="2.5"/><path d="M1.5 11.5a4.5 4.5 0 0 1 9 0"/></svg>
      My Account
    </div>
  </header>

  <nav class="navbar">
    <div class="brand"><span class="mark"></span>Pelmora Hearing</div>
    <div class="menu">
      <a class="active">Your Hearing</a>
      <a>Hearing Aids</a>
      <a>Musicians</a>
      <a>Doctors Information</a>
      <a>About Us</a>
      <a>Contact us</a>
    </div>
    <div class="search">
      <svg width="13" height="13" viewBox="0 0 13 13" fill="none" stroke="#666" stroke-width="1.3"><circle cx="5.5" cy="5.5" r="4.5"/><path d="M9 9l3.5 3.5"/></svg>
      Search
    </div>
  </nav>

  <section class="hero">
    <div class="hero-photo" role="img" aria-label="Photo of an audiologist in a white coat with a young girl in a pink top looking through an otoscope, bright clinic background"></div>
    <div class="hero-copy">
      <h1><span class="accent">A New Hearing</span><br>Health Experience</h1>
      <p>Check Out Our Services!</p>
      <div class="btn">CHECK OUT</div>
    </div>
    <div class="appointment">Make an Appointment
      <svg width="8" height="5" viewBox="0 0 8 5"><path d="M0 5L4 0l4 5z" fill="#fff"/></svg>
    </div>
  </section>

  <section class="welcome">
    <h2>Welcome to</h2>
    <h3>Pelmora Hearing</h3>
    <div class="bar"></div>
    <p>Pelmora Hearing is an independently owned and managed professional audiology clinic. Our Audiologists are health-care professionals specialising in diagnosing, treating and monitoring everything to do with hearing and balance. At Pelmora Hearing we work closely with Ear, Nose and Throat specialists to ensure you receive the highest standards of medical care.</p>
  </section>

  <article class="service s1">
    <svg viewBox="0 0 90 90" fill="none" stroke="#c2aca4" stroke-width="2.4">
      <circle cx="45" cy="45" r="43"/><circle cx="45" cy="45" r="36"/>
      <path d="M32 52v-6a13 13 0 0 1 26 0v6"/>
      <rect x="30" y="47" width="5" height="10" rx="1"/><rect x="55" y="47" width="5" height="10" rx="1"/>
    </svg>
    <h4>Audiological Evaluation</h4>
    <p>The first step begins with a proper audiological evaluation. The right hearing aid selection is made once we thoroughly understand your hearing loss and lifestyle needs.</p>
  </article>

  <article class="service s2">
    <svg viewBox="0 0 90 90" fill="none" stroke="#c2aca4" stroke-width="2.4">
      <circle cx="45" cy="45" r="43"/><circle cx="45" cy="45" r="36"/>
      <path d="M34 45l8 8 15-15" stroke-width="3"/>
    </svg>
    <h4>Hearing Aid Selection</h4>
    <p>The next step is to assist you in helping you make the appropriate hearing aid selection according to your technological needs as well as your financial needs.</p>
  </article>

  <article class="service s3">
    <svg viewBox="0 0 90 90" fill="none" stroke="#c2aca4" stroke-width="2.4">
      <circle cx="45" cy="45" r="43"/><circle cx="45" cy="45" r="36"/>
      <path d="M38 40a8 8 0 0 1 16 0c0 6-6 7-6 13a4 4 0 0 1-6 3"/>
    </svg>
    <h4>Custom Fitting Process</h4>
    <p>Lastly, our audiologists will listen intently to your feedback and then use all of our expertise and knowledge to ensure that your hearing aids are properly adjusted.</p>
  </article>

  <footer class="footer"></footer>
</body>
</html>
```